Simple, elegant, business card design required

Hi designers,I am looking for a simple yet elegant business card design.

Please make use of my logo (attached); you are free to tweak the logo should you wish to do so.

Our business is involved in many different fields - almost all of them involved in some form of "design", so that's really one of the key things I want to portray. I do not wish to specify which field of design, exactly.

I prefer white on black (or just monochromatic), but if you have a different, creative idea, I am open to that too.

You can use artsy photographs provided that you have the license to use those. Please feel free to ask me any questions.
Updates

Project Deadline Extended Reason: Small extension for potential revisions. Did not get the time to provide as much feedback as I can. Added Wednesday, July 09, 2014

Target Market(s)

High-end customers looking for design consultancy

Industry/Entity Type

Business

Contact Information for Business Card

Name: Gareth Moonfield
Position: Creative Director
Mobile: +155603928174
Address: Barrow Lane, Ashcombe upon Wyre, Glenmoreshire GL12 4RT
Website: torvakest.com (not launched yet)

Requirements
Must have
• Design layout must be clean, original, and text must be readable when printed.
Should not have
• ~ No business card templates please. Anyone using this will be reported.
• ~ Please don't spam entries.

```html
<!DOCTYPE html>
<html lang="en">
<head>
<meta charset="utf-8">
<title>Torvakest Business Card</title>
<link rel="stylesheet" href="https://fonts.googleapis.com/css2?family=PT+Sans:wght@400;700&display=swap">
<style>
  :root {
    --backdrop: #2f2f2f;
    --card: #ffffff;
    --ink: #231f20;
    --rule: #6d6d6d;
    --cream: #f7e7a6;
    --slate: #555555;
  }
  html, body {
    margin: 0;
    padding: 0;
    width: 1200px;
    height: 750px;
    overflow: hidden;
    background: var(--backdrop);
  }
  .canvas {
    position: relative;
    width: 1200px;
    height: 750px;
  }
  .card {
    position: absolute;
    left: 100px;
    top: 86px;
    width: 1000px;
    height: 578px;
    background: var(--card);
    border-radius: 40px;
    overflow: hidden;
    font-family: "PT Sans", sans-serif;
    color: var(--ink);
  }
  .brand-block {
    position: absolute;
    left: 50px;
    top: 44px;
    width: 281px;
    height: 161px;
    background: var(--ink);
  }
  .brand-name {
    position: absolute;
    left: 358px;
    top: 96px;
    margin: 0;
    font-size: 44px;
    font-weight: 400;
    letter-spacing: 7px;
    line-height: 1;
  }
  .person {
    position: absolute;
    right: 55px;
    top: 234px;
    text-align: right;
  }
  .person-name {
    margin: 0;
    font-size: 33px;
    font-weight: 700;
    line-height: 1.1;
  }
  .person-role {
    margin: 0;
    font-size: 27px;
    font-weight: 400;
    letter-spacing: 0.5px;
    line-height: 1.2;
  }
  .divider {
    position: absolute;
    left: 50px;
    top: 333px;
    width: 900px;
    height: 2px;
    background: var(--rule);
  }
  .address {
    position: absolute;
    left: 50px;
    top: 344px;
    font-size: 27px;
    line-height: 37px;
  }
  .address p { margin: 0 0 0 31px; }
  .address .pin {
    position: absolute;
    left: 0;
    top: 9px;
    width: 20px;
    height: 26px;
  }
  .contact {
    position: absolute;
    right: 55px;
    top: 381px;
    font-size: 27px;
    line-height: 37px;
    text-align: right;
  }
  .contact p { margin: 0; }
  .contact svg {
    width: 20px;
    height: 20px;
    margin-left: 12px;
    vertical-align: -2px;
  }
  .footer-band {
    position: absolute;
    left: 0;
    bottom: 0;
    width: 1000px;
    height: 108px;
    background: linear-gradient(to bottom, var(--cream) 0%, var(--slate) 45%, var(--ink) 100%);
  }
</style>
</head>
<body>
<div class="canvas">
  <section class="card">
    <div class="footer-band" role="img" aria-label="Decorative flowing band in cream, grey and black along the bottom edge"></div>

    <div class="brand-block"></div>
    <h1 class="brand-name">TORVAKEST</h1>

    <div class="person">
      <p class="person-name">Gareth Moonfield</p>
      <p class="person-role">Creative Director</p>
    </div>

    <div class="divider"></div>

    <div class="address">
      <svg class="pin" viewBox="0 0 20 26" aria-hidden="true">
        <path fill="var(--ink)" d="M10,0 C4.5,0 0,4.5 0,10 C0,17 10,26 10,26 C10,26 20,17 20,10 C20,4.5 15.5,0 10,0 Z M10,6 A4,4 0 1 1 10,14 A4,4 0 1 1 10,6 Z"/>
      </svg>
      <p>Barrow Lane</p>
      <p>Ashcombe upon Wyre</p>
      <p>Glenmoreshire GL12 4RT</p>
    </div>

    <div class="contact">
      <p>+155603928174<svg viewBox="0 0 20 20" aria-hidden="true"><rect x="4" y="1" width="12" height="18" rx="2" fill="none" stroke="var(--ink)" stroke-width="1.8"/><line x1="8" y1="16" x2="12" y2="16" stroke="var(--ink)" stroke-width="1.6"/></svg></p>
      <p>www.torvakest.com<svg viewBox="0 0 20 20" aria-hidden="true"><g fill="none" stroke="var(--slate)" stroke-width="1.4"><circle cx="10" cy="10" r="8.5"/><ellipse cx="10" cy="10" rx="3.8" ry="8.5"/><line x1="1.5" y1="10" x2="18.5" y2="10"/><line x1="3" y1="5.5" x2="17" y2="5.5"/><line x1="3" y1="14.5" x2="17" y2="14.5"/></g></svg></p>
    </div>
  </section>
</div>
</body>
</html>
```